Home Health Care Agency Needs a Website (Seeking a PSD)

We need a user friendly website for a Home Health Care Agency. Our service is for the elderly and disabled. Frequently the busy professional middle-aged married daughter will use the website to arrange in-home care for an aging parent. Therefore, our website is primarily geared towards middle-aged women. In-home care is typically 24 hours a day so, a feeling of trustworthiness and security should be effectively conveyed. (Seeking a PSD- however, if you also offer coding, please let us know the cost.)

Target Market(s)

Frequently the busy professional middle-aged married daughter (possibly out of state) will use the website to arrange in-home care for an aging parent.

Industry/Entity Type

Security

Requirements
Must have
• Website must be clean, uncluttered and professional. The following menu pages are requested: Home, About Us, Services, Resources, FAQ, Employment & Contact.
Should not have
• Must not be too whimsical.

```html
<!DOCTYPE html>
<html lang="en">
<head>
<meta charset="utf-8">
<title>Harbor Home Health</title>
<link href="https://fonts.googleapis.com/css2?family=Source+Sans+3:wght@300;400;600&display=swap" rel="stylesheet">
<style>
:root{
  --bg:#f3f3f3;
  --page:#ffffff;
  --blue:#3a95d4;
  --blue-light:#7ab8e0;
  --nav-top:#a6d5f4;
  --nav-bottom:#5eaae6;
  --ink:#4a4a4a;
  --ink-soft:#8a8a8a;
  --footer:#4a4849;
  --btn-top:#7a7a7a;
  --btn-bottom:#4b4b4b;
}
*{box-sizing:border-box;margin:0;padding:0}
html,body{width:1046px;height:1200px;overflow:hidden;background:var(--bg)}
body{font-family:"Source Sans 3",sans-serif;color:var(--ink)}
.stage{position:absolute;left:0;top:0;width:1208px;height:1386px;transform:scale(0.8659);transform-origin:0 0}
.page{position:absolute;left:100px;top:0;width:1024px;height:1386px;background:var(--page)}
.brand{position:absolute;left:28px;top:45px;display:flex;align-items:center;gap:12px}
.brand-mark{width:40px;height:40px;border-radius:50%;background:var(--blue-light)}
.brand-name{font-size:36px;font-weight:600;color:var(--blue-light);letter-spacing:-0.5px}
.call{position:absolute;right:26px;top:72px;text-align:right}
.call-label{font-size:19px;color:var(--blue-light);font-weight:400}
.call-number{font-size:31px;color:#555;font-weight:400;line-height:1}
.nav{position:absolute;left:0;top:141px;width:1024px;height:50px;background:linear-gradient(var(--nav-top),var(--nav-bottom));display:flex}
.nav a{color:#fff;text-decoration:none;font-size:20px;line-height:50px;padding:0 28px;border-right:1px solid rgba(40,110,170,.45);box-shadow:1px 0 0 rgba(255,255,255,.35)}
.nav a:first-child{padding-left:50px}
.nav a:last-child{border:none;box-shadow:none}
.hero{position:absolute;left:0;top:191px;width:1024px;height:404px;background:linear-gradient(90deg,#c9d6a8 0%,#e6e2cf 30%,#f2e6df 60%,#e9dcd8 100%)}
.hero-card{position:absolute;left:51px;top:148px;width:406px;height:164px;background:rgba(255,255,255,.9);border-radius:8px;padding:25px 16px 0 30px}
.hero-card h2{font-weight:300;color:var(--blue);font-size:26px;line-height:1.1;white-space:nowrap}
.hero-card h2 span{display:block;font-size:32px;font-weight:400;letter-spacing:-0.3px;line-height:1.15}
.hero-card p{color:var(--blue);font-size:16px;font-weight:300;margin-top:6px;line-height:1.4}
.dots{position:absolute;left:477px;top:377px;display:flex;gap:4px}
.dots i{width:15px;height:15px;border-radius:50%;background:#fff}
.dots i:first-child{background:#777}
.welcome{position:absolute;left:32px;top:638px;width:660px}
.welcome h1{font-weight:300;font-size:31px;color:#444}
.welcome h3{font-weight:300;font-size:19px;margin:6px 0 4px 3px;color:#444}
.welcome p{font-weight:300;font-size:14px;line-height:25px;color:var(--ink-soft);margin-left:3px}
.quote{position:absolute;left:717px;top:628px;width:275px;height:228px;border-radius:4px;background:linear-gradient(#8fcaf1,#5aa7e2);border:1px solid #4d98d3}
.quote h2{position:absolute;left:27px;top:18px;font-weight:400;font-size:24px;color:#1d5f95}
.quote .field{position:absolute;left:25px;width:223px;height:27px;background:#fff;border-radius:3px;font-size:13px;color:#777;padding:5px 12px;font-weight:300;line-height:17px}
.quote .f1{top:59px}
.quote .f2{top:96px}
.quote .f3{top:135px}
.quote .submit{position:absolute;right:23px;top:171px;width:90px;height:31px;border-radius:4px;background:linear-gradient(#ffffff,#d7ecfa);color:#1d6db0;font-size:17px;text-align:center;line-height:31px}
.rule{position:absolute;left:36px;top:900px;width:964px;border-top:1px dotted #aaa}
.card{position:absolute;top:940px;width:300px}
.card-photo{height:130px;border:1px solid #ddd;background:linear-gradient(90deg,#b9b3ab,#e0d8d2)}
.card h2{font-weight:400;font-size:24px;color:var(--blue);margin:9px 0 0 1px}
.card h4{font-weight:300;font-size:17px;color:#444;margin:4px 0 2px 1px}
.card p{font-weight:300;font-size:14px;line-height:22px;color:var(--ink-soft);margin-left:1px}
.btn{display:inline-block;margin-top:8px;height:29px;padding:0 15px;border-radius:4px;background:linear-gradient(var(--btn-top),var(--btn-bottom));color:#fff;font-size:14px;line-height:29px}
.footer{position:absolute;left:0;top:1273px;width:1024px;height:113px;background:var(--footer)}
.footer nav{position:absolute;left:43px;top:28px;color:#fff;font-size:15px}
.footer nav span{margin:0 6px;color:#ddd}
.footer small{position:absolute;left:40px;top:57px;color:#bbb;font-size:14px;font-weight:300}
.social{position:absolute;right:36px;top:27px;display:flex;gap:8px}
.social i{width:23px;height:23px;border-radius:3px;background:#8fb7d9}
.social i:last-child{background:#e88a3a}
</style>
</head>
<body>
<div class="stage">
 <div class="page">
  <div class="brand"><div class="brand-mark"></div><div class="brand-name">Harbor Home Health</div></div>
  <div class="call"><div class="call-label">CALL US NOW</div><div class="call-number">0700 555 0142</div></div>
  <nav class="nav"><a>Home</a><a>About Us</a><a>Services</a><a>Resources</a><a>FAQ</a><a>Employment</a><a>Contact</a></nav>
  <section class="hero" role="img" aria-label="Photo of a smiling elderly woman holding a carer's hand outdoors">
   <div class="hero-card">
    <h2>Provide Health Treatment<span>and Care to Elderly People</span></h2>
    <p>Class aptent taciti sociosqu ad litora torquent per<br>conubia nostra, per inceptos hymenaeos.</p>
   </div>
   <div class="dots"><i></i><i></i><i></i><i></i></div>
  </section>
  <section class="welcome">
   <h1>Welcome to Harbor Home Health Mainpage</h1>
   <h3>Duis tincidunt lectus quis dui viverra vestibulum Suspendisse vulputate</h3>
   <p>Nulla elementum dui ut augue. Aliquam vehicula mi at mauris. Maecenas placerat, nisl at consequat rhoncus, sem nunc gravida justo, quis eleifend arcu velit quis lacus. Morbi magna magna, tincidunt a, mattis non, imperdiet vitae, tellus. Sed odio est, auctor ac, sollicitudin in, consequat vitae, orci. Fusce id felis.<br>Vivamus porttitor, g, purus nisi eleifend libero, a tempus libero lectus feugiat felis. Morbi diam mauris, viverra in, gravida eu, mattis in, ante. Morbi eget arcu. Morbi porta, libero id ullamcorper nonummy,</p>
  </section>
  <aside class="quote">
   <h2>Request a Quote</h2>
   <div class="field f1">Your Name</div>
   <div class="field f2">Email address</div>
   <div class="field f3">Phone no.</div>
   <div class="submit">Submit</div>
  </aside>
  <div class="rule"></div>
  <article class="card" style="left:36px">
   <div class="card-photo" role="img" aria-label="Photo of a young carer with an elderly woman"></div>
   <h2>Our Treatment &amp; Care</h2><h4>Vivamus porttitor purus nisi</h4>
   <p>Eleifend libero, a tempus libero lectus feugiat felis.<br>Morbi diam mauris, viverra in, gravida eu</p>
   <span class="btn">Read More</span>
  </article>
  <article class="card" style="left:365px">
   <div class="card-photo" role="img" aria-label="Photo of two hands holding an elderly person's hand" style="background:linear-gradient(90deg,#e9dcd6,#c79a86,#eee6e2)"></div>
   <h2 style="margin-left:3px">Why Choose Us</h2><h4 style="margin-left:3px">Vivamus porttitor purus nisi</h4>
   <p style="margin-left:3px">Eleifend libero, a tempus libero lectus feugiat felis.<br>Morbi diam mauris, viverra in, gravida eu</p>
   <span class="btn" style="margin-left:3px">Read More</span>
  </article>
  <article class="card" style="left:692px">
   <div class="card-photo" role="img" aria-label="Photo of a nurse smiling with an elderly woman" style="background:linear-gradient(90deg,#9a9aa0,#c8c2bc,#e7e2dc)"></div>
   <h2 style="margin-left:6px">Services Provide</h2><h4 style="margin-left:6px">Vivamus porttitor purus nisi</h4>
   <p style="margin-left:6px">Eleifend libero, a tempus libero lectus feugiat felis.<br>Morbi diam mauris, viverra in, gravida eu</p>
   <span class="btn" style="margin-left:3px">Read More</span>
  </article>
  <footer class="footer">
   <nav>Home<span>|</span>About Us<span>|</span>Services<span>|</span>Resources<span>|</span>FAQ<span>|</span>Employment<span>|</span>Contact</nav>
   <small>© 2013 Company Name.&nbsp; All right reserved.&nbsp; Term of Use</small>
   <div class="social"><i></i><i></i><i></i><i></i></div>
  </footer>
 </div>
</div>
</body>
</html>
```